■ 依頼の目的/概要
グループ企業内で使用する、業務支援ポータルサイトのリニューアルです。
依頼内容は、TOPページのデザイン作成です。
レイアウト案が2パターンありますので、制作要項をもとに、合計2パターンご提案をお願いします。
(制作要項:P3~4参照)

■現在の参考サイト
制作要項に、参考URLを掲載しております。詳しくは添付の制作要項を参照ください。

■現状の課題
・デザインが洗練されていない。
・情報を伝達、共有するツールとしては分かり難いレイアウトの為、社員に情報が伝わりにくい。
・メニューが煩雑になっており、従業員が必要な情報を探すときにも、目的にたどり着きにくい。

■ 重視する点/検討基準
① デザイン性(使いやすさ・見やすさ・親しみやすさ)
② 納期厳守

■ 具体的な制作数
TOPページ:2パターン(デザイン) *制作要項:P.3~4参照

■募集条件
キャラクターにつきましては、商標上の問題により、現在開示することが出来ないため、
アタリで作成をお願い致します。
デザイン選定後、当選者にキャラクターデザインをお渡ししますので、
差し込んで頂き、納品完了となります。
ご認識をお願いします。

■納品ファイル
・イラストレーター形式(.ai)
・フォトショップ形式(.psd)
*1 募集条件を満たした状態のデザイン
*2 納品のフォトショップは、できるだけレイヤー結合せず、コーディング時に部品として
扱えるようにしてください。こちらでも再加工できる状態でお願いします。

■選考の進め方
ご提案頂いたデザイン内容・コンセプトなどをもとに、プロジェクトメンバーで選考、決定致します。

皆様からの、素晴らしいご提案を、お待ちしております。
宜しくお願い致します。
この度、募集期間を5日間、延長させて頂きます。
また、依頼金額についても 50,000円 ⇒ 70,000円 に変更致します。

今一度、ご提案を頂ければ幸甚です。引き続き、よろしくお願いします。
こちらが要望するデザインイメージと、使用していただくデザインパーツを加えております。
改めて、ご参照頂ますよう、お願いします。
コンセプトに見合うデザインは、ご提案頂いておりますが、あと1日延長させて頂きます。
引き続き、皆様からのご提案をお待ちしております。
宜しくお願い致します。
たくさんのご提案ありがとうございます。
もうすこしパターンを見てみたいため、3日間延長いたします。

宜しくお願い致します。
度々申し訳御座いません。
幾つか、イメージに則したデザインをご提案頂いておりますが、
提案数が少ないので、再度延長致します。

見ていて楽しくなるようなポータルサイトデザインのご提案をお待ちしております。
引き続き宜しくお願い致します。
度々の延長により、ご迷惑をおかけしております。
今回、デザインについて、様々なパターンから検討したかったのですが、
思うように提案が集まらなかった為、依頼金額の追加、
及び期間の延長を行なっております。

情報不足により、皆様のデザインスキルを引き出すことができなかったと思い、
今回、募集要項に、開示できる限りの情報を添えて、更新しております。
ご参照頂ければ幸いです。

皆様からの素晴らしい提案をお待ちしております。
お世話になっております。
度々、申し訳ございませんが、1週間延長致します。
開示可能な情報が少ない為、提案するに出来ない状況なのでは無いかと
思いますが、必要な情報や、ご質問等御座いましたら、お気軽にお申し
付けください。

宜しくお願い致します。
度々申し訳御座いません。
再度1週間延長します。
素晴らしい提案を頂いておりますが、採用にまでは至っていない状況です。

ポータルサイトの用途を伝えきれていないかもしれませんので、
基本機能を、以下に明示します。

①サービス窓口のオペレータが、お客様へ案内する際に活用できるサービス情報データベース
②研修担当者が新人教育・研修時に活用できるマニュアル等の教育支援ツール
③新人社員が、空いた時間にテストやマニュアルなどを活用できる自己学習支援ツール
④目標などの数値関連を開示し、他のオペレータとの競争環境をつくり上げる、目標支援ツール
⑤対応時に手本となる音声データや対応時の良い台本などが拝聴・閲覧ができるスキルアップ支援ツール
⑥オペレータが業務において、疑問点や不明点、改善提案などを行い、実際にサービス運営陣も回答ができるFAQツール

上記の6点を利用でき、アクセス数を伸ばせるような、クオリティの高いポータルサイトデザインを募集致します。

ご質問のある方は、メッセージにて個別に回答致しますので、お気軽にお申し付けください。

引き続き、宜しくお願い致します。
本依頼に対しまして、お忙しい中、数々のデザインをご提案頂き、
誠にありがとうございました。
皆様からご提案頂いた貴重なデザイン案は、現在こちらで検討させて
頂いております。

今回の依頼は、スタート時点から、具体的な完成形が見えにくい依頼と
なっており、募集期限が大幅に伸び、Toviraの皆様方にはご迷惑をお掛け
致しました。
申し訳ございませんでした。

つきましては、完成形により具体性を持たせるため、弊社でデザインイメージを
作成致しました。
お手数をお掛けしますが、修正箇所は添付ファイルのデザインイメージ下部に
記載しておりますので、ご確認をお願い致します。

また、恐れ入りますが、依頼期限は12/28(金)まで、延長させて頂きたいと
思います。
素敵なデザイン案を、ご検討頂けますと幸甚です。

宜しくお願い申し上げます。

こちらの要望した、楽しげで、飽きの来ないデザインに加え、
ピンクを基調としたサイトカラーと、フェルト調のデザインパーツが
マッチしており、細部にこだわりを感じられるデザインになっていました。

まず、今回の依頼について、こちらの要望がうまく定まらず、ご迷惑をお掛けしたこと、お詫び申し上げます。
また、度重なる延長にも関わらず、ご協力頂きましたトヴィラの皆さまに感謝致します。誠にありがとうございました。

今後も、Tovirasを通して仕事を依頼する機会があるかと思いますが、その際はまた、素晴らしいご提案を頂ければ幸甚でございます。

```html
<!DOCTYPE html>
<html lang="ja">
<head>
<meta charset="utf-8">
<title>業務支援ポータル TOP</title>
<link href="https://fonts.googleapis.com/css2?family=M+PLUS+Rounded+1c:wght@500;800&family=Noto+Sans+JP:wght@400;700&display=swap" rel="stylesheet">
<style>
:root{
  --pink:#e8528a;--pink-soft:#fbe3ec;--pink-band:#fdf0f4;
  --blue:#3f9fd8;--blue-soft:#dcf0fa;
  --orange:#f29a2e;--green:#7cbf3f;--gray:#8a8a8a;
  --cream:#fdf4d8;--gold:#e9b949;--ink:#444;--line:#e3e3e3;
  --bear:#efc98c;
}
*{box-sizing:border-box;margin:0;padding:0}
html,body{width:684px;height:1200px;overflow:hidden;background:#fff}
body{position:relative;font-family:"Noto Sans JP",sans-serif;color:var(--ink);font-size:8px;line-height:1.3}
.round{font-family:"M PLUS Rounded 1c",sans-serif}
.abs{position:absolute}
ul{list-style:none}

.site-header{left:0;top:0;width:684px;height:50px;border-bottom:2px solid var(--pink-soft)}
.logo{left:14px;top:12px;display:flex;align-items:center;gap:6px;font-family:"M PLUS Rounded 1c",sans-serif;font-weight:800;font-size:14px;color:var(--pink)}
.logo i{width:14px;height:14px;border-radius:50%;background:var(--pink)}
.global-nav{left:160px;top:17px;display:flex;gap:26px;font-size:10px;font-weight:700}
.global-nav span{color:var(--ink)}

.hero{left:10px;top:62px;width:664px;height:144px;background:var(--cream);border-radius:4px}
.hero-art{left:10px;top:70px;width:215px;height:128px;background:linear-gradient(135deg,#f7d98a,var(--gold));border-radius:6px}
.hero-title{left:72px;top:104px;width:160px;padding:8px;background:#fff;border:2px solid var(--pink);border-radius:6px;color:var(--pink);font-family:"M PLUS Rounded 1c",sans-serif;font-weight:800;font-size:13px;line-height:1.35}
.hero-title small{display:block;font-size:10px}
.hero-copy{left:250px;top:80px;width:410px}
.hero-copy h2{font-size:11.5px;font-weight:700;margin-bottom:10px}
.hero-copy li{font-size:8px;line-height:1.6}
.pager{left:0;top:214px;width:684px;display:flex;justify-content:center;align-items:center;gap:8px}
.pager b{width:6px;height:6px;border-radius:50%;background:#ccc}
.pager b.on{background:var(--pink)}
.pager svg{width:8px;height:8px}
.rule{left:10px;top:234px;width:664px;height:1px;background:var(--line)}

.panel-head{height:24px;line-height:24px;padding-left:10px;font-weight:700;font-size:10px;border-radius:3px 3px 0 0}
.purpose{left:12px;top:250px;width:428px;height:106px;border:1px solid var(--line);border-radius:4px}
.purpose .panel-head{background:var(--pink-soft);color:var(--pink)}
.purpose-cols{display:flex;padding:8px 8px 0}
.purpose-col{flex:1}
.purpose-col h3{display:inline-block;font-size:8px;color:#fff;padding:1px 8px;border-radius:8px;margin-bottom:4px}
.purpose-col li{font-size:7px;line-height:1.5}
.purpose-col li::before{content:"▸ ";color:var(--gray)}

.mascot{width:56px;height:66px;background:var(--bear);border-radius:28px 28px 10px 10px}
.section-title{font-family:"M PLUS Rounded 1c",sans-serif;font-weight:800;font-size:12px;color:var(--pink)}
.section-line{height:1px;background:var(--pink-soft)}
.feed{width:428px}
.feed li{display:flex;align-items:center;height:24px;border-bottom:1px dotted var(--line);font-size:7.5px}
.feed .date{width:46px;color:var(--gray)}
.feed .tag{width:18px;height:8px;border-radius:2px;margin-right:8px}
.feed .title{flex:1}
.feed .mark{font-size:7px;font-weight:700}

.side{left:463px;width:210px}
.side-search .panel-head{background:var(--blue-soft);color:var(--blue)}
.search-box{margin-top:4px;height:18px;border:1px solid var(--line);border-radius:2px;font-size:7px;color:#aaa;padding:3px 6px}
.ranking .panel-head{background:var(--pink-soft);color:var(--pink)}
.ranking li{display:flex;align-items:center;height:19px;border-bottom:1px dotted var(--line);font-size:8.5px}
.ranking li span{width:26px;font-size:7px;color:var(--gray);padding-left:6px}
.ranking li.top{font-size:11px;font-weight:700}
.ranking li.top span{color:var(--pink)}
.bookmarks .panel-head{background:var(--blue-soft);color:var(--blue)}
.bookmarks li{height:20px;line-height:20px;border-bottom:1px dotted var(--line);font-size:7px;padding-left:6px}

.site-footer{left:0;top:1066px;width:684px;height:100px;background:var(--pink-band);border-top:2px solid var(--pink-soft)}
.footer-cols{left:24px;top:1076px;display:flex;gap:50px}
.footer-cols h4{font-size:8.5px;margin-bottom:4px}
.footer-cols li{font-size:7px;line-height:1.6}
.copyright{left:14px;top:1174px;font-size:6.5px;color:var(--gray)}
.footer-links{right:14px;top:1174px;font-size:6.5px;color:var(--gray)}
</style>
</head>
<body>

<header class="site-header abs"></header>
<div class="logo abs"><i></i>ハナモリ ポータル</div>
<nav class="global-nav abs"><span>学ぶ</span><span>機能を使う</span><span>業務知識</span><span>日報・成績</span><span>お問合わせ</span></nav>

<section class="hero abs"></section>
<div class="hero-art abs" role="img" aria-label="リボン付きのギフトボックスとキャラクターのイラスト"></div>
<div class="hero-title abs">業務連絡の効率化について<small>（メールの件名統一化）</small></div>
<div class="hero-copy abs">
  <h2>社内の業務効率化を図るため、メールの件名をルール化致します。</h2>
  <ul>
    <li>(1) 業務用件の場合は、【業務連絡】</li>
    <li>(2) 業務用件の場合は、【業務連絡】</li>
    <li>(3) 業務用件の場合は、【業務連絡】</li>
    <li>(4) 業務用件の場合は、【業務連絡】</li>
    <li>ご協議のうえ、件名から実施をお願いします。よろしくお願いします。　運営事務局</li>
  </ul>
</div>
<div class="pager abs">
  <svg viewBox="0 0 8 8"><path d="M6 0L1 4l5 4z" fill="#999"/></svg>
  <b></b><b></b><b class="on"></b><b></b><b></b>
  <svg viewBox="0 0 8 8"><path d="M2 0l5 4-5 4z" fill="#999"/></svg>
</div>
<div class="rule abs"></div>

<section class="purpose abs">
  <div class="panel-head round">目的から探す</div>
  <div class="purpose-cols">
    <div class="purpose-col"><h3 style="background:var(--blue)">関連を調べる</h3><ul><li>規約から</li><li>機能から</li><li>サービスから</li></ul></div>
    <div class="purpose-col"><h3 style="background:var(--pink)">学ぶ</h3><ul><li>研修資料から</li><li>対応フローを見る</li><li>よくある質問を見る</li><li>今月度の模擬テスト</li><li>過去の模擬テスト</li></ul></div>
    <div class="purpose-col"><h3 style="background:var(--orange)">機能を使う</h3><ul><li>メッセージを送る</li><li>提供したファイルを見る</li><li>マイページへ</li></ul></div>
    <div class="purpose-col"><h3 style="background:var(--green)">成績の確認</h3><ul><li>成績A</li><li>成績B</li><li>成績C</li><li>成績D</li></ul></div>
  </div>
</section>

<div class="mascot abs" style="left:14px;top:364px" role="img" aria-label="キャラクターのアタリ"></div>
<h2 class="section-title abs" style="left:78px;top:400px">新着連絡</h2>
<div class="section-line abs" style="left:12px;top:424px;width:428px"></div>
<ul class="feed abs" style="left:12px;top:430px">
  <li><span class="date">10月18日</span><i class="tag" style="background:var(--pink)"></i><span class="title">【業務連絡】業務連絡の効率化について（メールの件名統一化）</span><span class="mark" style="color:var(--pink)">受付A</span></li>
  <li><span class="date">10月5日</span><i class="tag" style="background:var(--blue)"></i><span class="title">【業務連絡】業務連絡の効率化について（メールの件名統一化）</span><span class="mark" style="color:var(--blue)">受付B</span></li>
  <li><span class="date">10月4日</span><i class="tag" style="background:var(--green)"></i><span class="title">【業務連絡】業務連絡の効率化について（メールの件名統一化）</span><span class="mark" style="color:var(--green)">受付C</span></li>
  <li><span class="date">9月30日</span><i class="tag" style="background:var(--orange)"></i><span class="title">【業務連絡】業務連絡の効率化について（メールの件名統一化）</span><span class="mark" style="color:var(--pink)">受付A</span></li>
  <li><span class="date">9月28日</span><i class="tag" style="background:var(--pink)"></i><span class="title">【業務連絡】業務連絡の効率化について（メールの件名統一化）</span><span class="mark" style="color:var(--blue)">受付B</span></li>
  <li><span class="date">9月25日</span><i class="tag" style="background:var(--blue)"></i><span class="title">【業務連絡】業務連絡の効率化について（メールの件名統一化）</span><span class="mark" style="color:var(--pink)">受付A</span></li>
  <li><span class="date">9月20日</span><i class="tag" style="background:var(--green)"></i><span class="title">【業務連絡】業務連絡の効率化について（メールの件名統一化）</span><span class="mark" style="color:var(--green)">受付C</span></li>
  <li><span class="date">9月12日</span><i class="tag" style="background:var(--pink)"></i><span class="title">【業務連絡】業務連絡の効率化について（メールの件名統一化）</span><span class="mark" style="color:var(--pink)">受付A</span></li>
  <li><span class="date">9月8日</span><i class="tag" style="background:var(--orange)"></i><span class="title">【業務連絡】業務連絡の効率化について（メールの件名統一化）</span><span class="mark" style="color:var(--blue)">受付B</span></li>
  <li><span class="date">9月2日</span><i class="tag" style="background:var(--blue)"></i><span class="title">【業務連絡】業務連絡の効率化について（メールの件名統一化）</span><span class="mark" style="color:var(--pink)">受付A</span></li>
</ul>

<div class="mascot abs" style="left:14px;top:688px" role="img" aria-label="キャラクターのアタリ"></div>
<h2 class="section-title abs" style="left:78px;top:730px">障害・メンテナンス情報</h2>
<div class="section-line abs" style="left:12px;top:754px;width:428px"></div>
<ul class="feed abs" style="left:12px;top:760px">
  <li><span class="date">10月10日</span><i class="tag" style="background:var(--pink)"></i><span class="title">【業務連絡】業務連絡の効率化について（メールの件名統一化）</span><span class="mark" style="color:var(--pink)">受付A</span></li>
  <li><span class="date">10月4日</span><i class="tag" style="background:var(--blue)"></i><span class="title">【業務連絡】業務連絡の効率化について（メールの件名統一化）</span><span class="mark" style="color:var(--blue)">受付B</span></li>
  <li><span class="date">9月30日</span><i class="tag" style="background:var(--green)"></i><span class="title">【業務連絡】業務連絡の効率化について（メールの件名統一化）</span><span class="mark" style="color:var(--pink)">受付A</span></li>
  <li><span class="date">9月21日</span><i class="tag" style="background:var(--orange)"></i><span class="title">【業務連絡】業務連絡の効率化について（メールの件名統一化）</span><span class="mark" style="color:var(--blue)">受付B</span></li>
  <li><span class="date">9月18日</span><i class="tag" style="background:var(--pink)"></i><span class="title">【業務連絡】業務連絡の効率化について（メールの件名統一化）</span><span class="mark" style="color:var(--pink)">受付A</span></li>
  <li><span class="date">9月12日</span><i class="tag" style="background:var(--blue)"></i><span class="title">【業務連絡】業務連絡の効率化について（メールの件名統一化）</span><span class="mark" style="color:var(--green)">受付C</span></li>
  <li><span class="date">9月7日</span><i class="tag" style="background:var(--green)"></i><span class="title">【業務連絡】業務連絡の効率化について（メールの件名統一化）</span><span class="mark" style="color:var(--pink)">受付A</span></li>
  <li><span class="date">9月3日</span><i class="tag" style="background:var(--pink)"></i><span class="title">【業務連絡】業務連絡の効率化について（メールの件名統一化）</span><span class="mark" style="color:var(--blue)">受付B</span></li>
  <li><span class="date">8月30日</span><i class="tag" style="background:var(--orange)"></i><span class="title">【業務連絡】業務連絡の効率化について（メールの件名統一化）</span><span class="mark" style="color:var(--pink)">受付A</span></li>
</ul>

<aside class="side side-search abs" style="top:250px">
  <div class="panel-head round">検索</div>
  <div class="search-box">キーワードを入力</div>
</aside>
<aside class="side ranking abs" style="top:306px">
  <div class="panel-head round">今週の検索キーワード TOP10</div>
  <ul>
    <li class="top"><span>1位</span>手続き</li>
    <li class="top"><span>2位</span>契約</li>
    <li class="top"><span>3位</span>料金</li>
    <li><span>4位</span>申し込み</li>
    <li><span>5位</span>引越し</li>
    <li><span>6位</span>名義変更</li>
    <li><span>7位</span>商品</li>
    <li><span>8位</span>解約</li>
    <li><span>9位</span>シリーズ</li>
    <li><span>10位</span>食べ物</li>
  </ul>
</aside>
<aside class="side bookmarks abs" style="top:548px">
  <div class="panel-head round">サイト内ブックマーク</div>
  <ul>
    <li>【業務連絡】業務連絡 連絡タイトル</li>
    <li>【業務連絡】業務連絡 連絡タイトル</li>
    <li>【対応フロー】基本フロー タイトル</li>
    <li>【対応フロー】基本フロー タイトル</li>
    <li>【研修資料】新人研修 資料タイトル</li>
    <li>【業務連絡】業務連絡 連絡タイトル</li>
    <li>【対応フロー】基本フロー タイトル</li>
    <li>【対応フロー】フロータイトル タイトル</li>
  </ul>
</aside>

<footer class="site-footer abs"></footer>
<div class="footer-cols abs">
  <div><h4 style="color:var(--pink)">学ぶ</h4><ul><li>研修テスト</li><li>新規テスト</li><li>対応フローチャート</li></ul></div>
  <div><h4 style="color:var(--blue)">機能を使う</h4><ul><li>メッセージー</li><li>ファイルボックス</li><li>ガジェット</li></ul></div>
  <div><h4 style="color:var(--orange)">業務知識</h4><ul><li>教材</li><li>カテゴリ</li><li>設計資料</li></ul></div>
  <div><h4 style="color:var(--green)">日報・成績</h4><ul><li>日報</li><li>成績</li><li>その他</li></ul></div>
  <div><h4 style="color:var(--gray)">お問合わせ</h4><ul><li>運営者へ</li><li>運営先へ</li><li>不明へ</li></ul></div>
</div>
<p class="copyright abs">© 2011 Hanamori Corporation. All rights reserved.</p>
<p class="footer-links abs">社内規約 ｜ プライバシーポリシー</p>

</body>
</html>
```